Venlox - Property Management Company Listings - PSD / uncoded only

Our site simply connects property owners with property managers. I’m asking you to create 2 pages, 1 homepage and 1 page that lists of property management companies. Build with Responsive Design in mind. PSD/uncoded files only. Help us create a great site!
Example competitor sites:
http://www.everyestatehelp.example/
http://www.tendyourlots.example/
Inspired by these sites:
http://www.quorvik.example/
http://www.bespokely.example/
http://www.coinwire.example/
https://www.tripboard.example/
I've attached the logo as well as 2 picture files that you can consider using.
• Venlox Logo Colors: Yellow: HTML code: #FBC30A, RGB code: R: 251 G: 195 B: 10 Grey: HTML code: #4E4C4D, RGB code: R: 78 G: 76 B: 77
• The picture files are optional.
o One picture is of houses and neighborhood.
o The other is of a professional woman on the phone. Please do not use the professional woman as a large primary image. You can use the professional woman photo as a smaller photo and not the main photo.
• Please bring your own pictures and graphics too. Don't feel like you need to use mine.
Thank you!

```html
<!DOCTYPE html>
<html lang="en">
<head>
<meta charset="utf-8">
<title>Venlox — Property Management</title>
<link href="https://fonts.googleapis.com/css2?family=Questrial&family=Montserrat:wght@700&family=PT+Sans:wght@400;700&display=swap" rel="stylesheet">
<style>
:root{
  --yellow:#fbc30a;
  --nav:#fcc800;
  --gold:#e0b50f;
  --grey:#4e4c4d;
  --dark:#3f3f3f;
  --darker:#222;
  --panel:#464646;
  --light:#efefef;
  --text:#333;
}
*{box-sizing:border-box;margin:0;padding:0}
html,body{width:841px;height:1200px;overflow:hidden;background:#fff}
body{position:relative;font-family:Arial,Helvetica,sans-serif;color:var(--text)}
.abs{position:absolute}
.header{top:0;left:0;width:841px;height:115px}
.brand{left:72px;top:28px;font-family:'Montserrat',sans-serif;font-weight:700;font-size:50px;color:var(--grey);letter-spacing:-1px;display:flex;align-items:center;gap:10px}
.brand .mark{width:16px;height:16px;background:var(--yellow)}
.social-label{left:553px;top:40px;font-family:'Questrial',sans-serif;font-weight:700;font-size:15px;color:#111;letter-spacing:.5px}
.social{left:659px;top:36px;display:flex;gap:5px}
.social span{width:24px;height:24px;border-radius:50%}
.call{left:576px;top:76px;font-family:'Questrial',sans-serif;font-size:15px;color:#111;display:flex;align-items:center;gap:6px}
.call b{font-weight:700}
.nav{top:115px;left:0;width:841px;height:31px;background:var(--nav);border-bottom:1px solid #d9a800;font-family:'Questrial',sans-serif;font-size:14px;color:#222}
.nav a{position:absolute;top:7px;color:#222;text-decoration:none}
.nav .sep{position:absolute;top:0;width:1px;height:30px;background:#e6b600}
.nav .current::after{content:"";position:absolute;left:50%;top:24px;margin-left:-4px;border:4px solid transparent;border-bottom-color:#fff}
.hero{top:146px;left:0;width:841px;height:345px;background:linear-gradient(90deg,#3f6a2a 0%,#2f5a3a 20%,#3c6f7a 80%,#2f6b78 100%)}
.hero-photo{left:70px;top:14px;width:701px;height:300px;border:3px solid #fff;background:linear-gradient(180deg,#6d8f4a 0%,#8a8a8c 35%,#6f6c72 70%,#8b8581 100%)}
.dots{left:384px;top:327px;display:flex;gap:6px}
.dots span{width:8px;height:8px;border-radius:50%;background:#fff}
.dots span:first-child{background:var(--yellow)}
.search-band{top:491px;left:0;width:841px;height:107px;background:var(--light)}
.search{left:70px;top:27px;width:701px;height:55px;background:var(--panel);border-radius:4px;font-family:'PT Sans',sans-serif;font-size:13px;color:#fff}
.search label{position:absolute;top:20px}
.select{position:absolute;top:17px;width:158px;height:23px;background:#fff;border-radius:3px}
.select::after{content:"";position:absolute;right:9px;top:9px;border:5px solid transparent;border-top-color:#444}
.search .go{position:absolute;left:576px;top:14px;width:95px;height:27px;background:linear-gradient(#fcd134,#f0b800);border-radius:2px;color:#222;font-weight:700;font-size:12px;text-align:center;line-height:27px;letter-spacing:.5px}
.welcome{top:598px;left:0;width:841px;height:140px;text-align:center}
.welcome h1{margin-top:24px;font-family:'Questrial',sans-serif;font-weight:400;font-size:22px;color:#333;letter-spacing:.5px}
.welcome h1 b{font-family:'PT Sans',sans-serif;font-weight:700}
.welcome p{width:700px;margin:13px auto 0;font-size:9.5px;line-height:15px;color:#333}
.connect{top:738px;left:0;width:841px;height:295px;background:var(--gold)}
.connect .notch{left:405px;top:0;border:13px solid transparent;border-top-color:#fff;border-bottom:0}
.connect h2{position:absolute;top:28px;width:841px;text-align:center;font-family:'Montserrat',sans-serif;font-size:19.5px;color:#111;letter-spacing:-.4px}
.connect-photo{left:70px;top:73px;width:355px;height:184px;border:2px solid #fff;background:linear-gradient(90deg,#c9c6bf 0%,#e4e0d8 45%,#3a3a3c 70%,#d6d1c7 100%)}
.join{left:454px;top:69px;width:300px;font-family:'Questrial',sans-serif;color:#111}
.join h3{font-weight:400;font-size:19.5px}
.join h4{font-weight:400;font-size:16px;margin-top:1px;letter-spacing:.3px}
.join p{font-family:Arial,sans-serif;font-size:9.8px;line-height:15.4px;margin-top:8px;padding-left:2px;width:275px}
.btn-more{left:459px;top:228px;width:84px;height:26px;background:#333;border-radius:3px;color:#fff;font-size:11px;text-align:center;line-height:26px}
.footer{top:1033px;left:0;width:841px;height:143px;background:var(--dark);color:#fff}
.footer h5{position:absolute;top:22px;font-family:'PT Sans',sans-serif;font-weight:400;font-size:15px}
.footer ul{position:absolute;top:50px;list-style:none;font-size:9.5px}
.quick li{margin-bottom:5.7px;padding-left:11px;position:relative}
.quick li::before{content:"»";position:absolute;left:0;font-size:9px}
.follow li{display:flex;align-items:center;gap:6px;margin-bottom:5.5px;font-size:9px}
.follow i{width:14px;height:14px;border-radius:2px;display:inline-block}
.quote{left:384px;top:50px;width:180px;font-size:9px;line-height:11.3px;padding-left:11px}
.quote .q{position:absolute;font-family:Georgia,serif;font-size:16px;font-style:italic}
.news{left:595px;top:49px;width:175px;height:27px;background:#fff}
.news .btn{position:absolute;right:0;top:0;width:23px;height:27px;background:var(--yellow)}
.footer-brand{left:638px;top:88px;font-family:'Montserrat',sans-serif;font-weight:700;font-size:38px;color:#fff;letter-spacing:-1px}
.bottom{top:1176px;left:0;width:841px;height:24px;background:var(--darker);color:#fff;font-size:8.5px;text-align:center;line-height:24px}
</style>
</head>
<body>
<header class="abs header">
  <div class="abs brand"><span class="mark"></span>Venlox</div>
  <div class="abs social-label">Social Media</div>
  <div class="abs social">
    <span style="background:#1e4a7c"></span><span style="background:#29a9e1"></span><span style="background:#f39c1a"></span><span style="background:#d42b23"></span>
  </div>
  <div class="abs call">
    <svg width="12" height="14" viewBox="0 0 12 14"><path d="M3 0 L5 3 L3.6 4.6 Q5 8.5 8 10 L9.4 8.6 L12 10.8 L10.2 13.4 Q3 12 0.3 2 Z" fill="#222"/></svg>
    <b>Call Now :</b> 000-555-0148
  </div>
</header>

<nav class="abs nav">
  <a class="current" href="#" style="left:87px">Home</a>
  <span class="sep" style="left:156px"></span>
  <a href="#" style="left:186px">Are you a Property Manager</a>
  <span class="sep" style="left:399px"></span>
  <a href="#" style="left:430px">Contact Us</a>
</nav>

<section class="abs hero">
  <div class="abs hero-photo" role="img" aria-label="Aerial photo of a suburban neighbourhood of houses"></div>
  <div class="abs dots"><span></span><span></span><span></span><span></span></div>
</section>

<section class="abs search-band">
  <div class="abs search">
    <label style="left:23px">Select Your Property</label>
    <div class="select" style="left:147px"></div>
    <label style="left:321px">In Zipcode</label>
    <div class="select" style="left:399px"></div>
    <div class="go">SEARCH</div>
  </div>
</section>

<section class="abs welcome">
  <h1>WELCOME TO <b>VENLOX</b></h1>
  <p>Lorem ipsum dolor sit amet, consectetur adipiscing elit, sed do eiusmod tempor incididunt ut labore et dolore magna aliqua. Ut enim ad minim veniam, quis nostrud exercitation ullamco laboris nisi ut aliquip ex ea commodo consequat. Duis aute irure dolor in reprehenderit in voluptate velit esse cillum dolore eu fugiat nulla pariatur. Excepteur sint occaecat cupidatat non proident, sunt in culpa qui officia deserunt mollit anim id est laborum.</p>
</section>

<section class="abs connect">
  <div class="abs notch"></div>
  <h2>Connecting property owners with property managers</h2>
  <div class="abs connect-photo" role="img" aria-label="Photo of a professional woman talking on the phone"></div>
  <div class="abs join">
    <h3>Join Our Real Estate Property</h3>
    <h4>management company network.</h4>
    <p>Lorem ipsum dolor sit amet, consectetur adipiscing elit, sed do eiusmod tempor incididunt ut labore et dolore magna aliqua. Ut enim ad minim veniam, quis nostrud exercitation ullamco laboris nisi ut aliquip ex ea commodo consequat. Duis aute irure dolor in reprehenderit in voluptate velit esse deserunt mollit anim id est laborum...</p>
  </div>
  <div class="abs btn-more">read more</div>
</section>

<footer class="abs footer">
  <h5 style="left:76px">Quick Links</h5>
  <ul class="quick" style="left:76px">
    <li>Holiday Packages</li><li>Dubai Tours</li><li>Bookings</li><li>Enquiry</li><li>Contact Us</li>
  </ul>
  <h5 style="left:229px">Connect Us</h5>
  <ul class="follow" style="left:229px;top:49px">
    <li><i style="background:#3b5b99"></i>Follow us Friendwall</li>
    <li><i style="background:#4fb3e6"></i>Follow us Chirpline</li>
    <li><i style="background:#2a79b1"></i>Follow us Linkfold</li>
    <li><i style="background:#c8312b"></i>Viewtube</li>
  </ul>
  <h5 style="left:386px">Testimonial</h5>
  <div class="abs quote">
    <span class="q" style="left:-12px;top:-4px">“</span>
    When looking at its layout. The point of using Lorem Ipsum is that it has a more-or-less normal distribution of letters, as opposed to using 'Content here, content here', making it look like readable English.
    <span class="q" style="position:relative;top:4px">”</span>
  </div>
  <h5 style="left:594px">Join Our Newsletter</h5>
  <div class="abs news"><div class="btn">
    <svg width="23" height="27" viewBox="0 0 23 27"><circle cx="10" cy="11" r="4" fill="none" stroke="#fff" stroke-width="2"/><path d="M13 14 L17 18" stroke="#fff" stroke-width="2.4"/></svg>
  </div></div>
  <div class="abs footer-brand">Venlox</div>
</footer>

<div class="abs bottom">Copyright © Hollowmere.example 2003-2014 | Solution by Brindle Studio Website Design</div>
</body>
</html>
```